qTorvix - A forward thinking technology company in the greater Silicon Valley

A .ppt slide deck for a software consulting company. This slide deck will be used for project kick off meetings, sales proposals, and presentations to large audiences that report progress on a variety of projects. It should catch the eye with appealing creativity. Allow for flexibility in space and display. Project well both virtually and in person under varying light conditions. The finished product should give the impression that we are a custom shop but balance in appeal to larger, more traditional companies.

Review of the designs has been delayed due to holiday travel. Thank you for your submissions. I look forward to getting back to you the week of December 3rd.

Target Market(s)

We are an innovative technology company in the greater Silicon Valley. We design and build custom business analytics tools for large, retail corporations. Our solutions deal primarily in the supply chain space but we are leaning towards commercial construction and telecommunications industries. We are targeting prospective clients interested in machine learning and artificial intelligence. Our customers know quality and will pay for a custom solution that exceeds their expectations.

Industry/Entity Type

Business Software

Font styles to use
Sans Serif

Colors

Designer to choose colors to be used in the design.

Requirements
Must have
• Color, graphics, and photos. Multiple different template pages to appeal for graphs, pictures, text, or timelines.
Should not have
• Anything that resembles a "fidget spinner."

```html
<!DOCTYPE html>
<html lang="en">
<head>
<meta charset="utf-8">
<title>qTorvix Slide Deck Template</title>
<link href="https://fonts.googleapis.com/css2?family=Montserrat:wght@500;600;700&family=Open+Sans:wght@400;600&display=swap" rel="stylesheet">
<style>
:root{
  --teal:#3b8b9c;
  --teal-dark:#2f7584;
  --green:#8cc63f;
  --green-soft:#eef5df;
  --ink:#555a5e;
  --ink-soft:#7b8085;
  --line:#d7dadd;
  --paper:#ffffff;
  --stage-top:#f1f1f1;
  --stage:#9b9b9b;
}
*{box-sizing:border-box;margin:0;padding:0}
html,body{width:1200px;height:2707px;overflow:hidden}
body{font-family:"Open Sans",Arial,sans-serif;color:var(--ink);background:var(--stage)}
.hero{position:absolute;left:0;top:0;width:1200px;height:800px;background:var(--stage-top)}
.hero .slide{position:absolute;left:100px;top:110px;transform:scale(1.852);transform-origin:0 0;box-shadow:0 4px 10px rgba(0,0,0,.12)}
.deck{position:absolute;left:0;top:800px;width:1200px;height:1907px;display:grid;grid-template-columns:540px 540px;column-gap:50px;row-gap:70px;padding:48px 35px 0}
.slide{position:relative;width:540px;height:304px;background:var(--paper);overflow:hidden;box-shadow:0 3px 8px rgba(0,0,0,.25)}
.abs{position:absolute}
.brand{position:absolute;display:flex;align-items:center;gap:5px;font-family:"Montserrat",sans-serif;font-weight:600;color:var(--ink);font-size:12px;letter-spacing:.5px}
.brand i{display:block;width:8px;height:8px;background:var(--green)}
.heading{position:absolute;left:16px;top:12px;font-family:"Montserrat",sans-serif;font-weight:700;font-size:15px;color:var(--ink-soft)}
.heading b{color:var(--green)}
.top-rule{position:absolute;left:0;right:0;top:38px;height:1px;background:var(--line)}
.footer{position:absolute;left:16px;right:16px;bottom:10px;border-top:1px solid var(--line);font-size:5px;color:var(--ink-soft);padding-top:3px}
.pageno{position:absolute;right:14px;bottom:6px;width:12px;height:12px;border-radius:50%;background:var(--teal);color:#fff;font-size:5.5px;display:flex;align-items:center;justify-content:center}
.body{font-size:6px;line-height:1.55;color:var(--ink-soft)}
.sub{font-family:"Montserrat",sans-serif;font-weight:700;font-size:5.5px;color:var(--teal)}
.photo{position:absolute}
.btn{position:absolute;background:var(--teal);color:#fff;font-family:"Montserrat",sans-serif;font-weight:600;font-size:7px;text-align:center;line-height:16px}
.bullets{list-style:none}
.bullets li{position:relative;padding-left:12px;margin-bottom:6px}
.bullets li::before{content:"";position:absolute;left:0;top:2px;width:4px;height:4px;border-right:1.5px solid var(--green);border-top:1.5px solid var(--green);transform:rotate(45deg)}
.title{font-family:"Montserrat",sans-serif;font-weight:700;color:var(--teal);font-size:17px}
</style>
</head>
<body>

<section class="hero">
  <div class="slide slide-title">
    <div class="brand" style="left:22px;top:20px;font-size:14px"><i></i>qTorvix</div>
    <div class="abs" style="left:22px;top:40px;font-size:5.5px;color:var(--green);font-weight:600">Your Partner for Innovative Software Solutions</div>
    <div class="abs title" style="left:280px;top:22px">PRESENTATION TITLE</div>
    <div class="abs" style="left:280px;top:46px;width:260px;height:1px;background:var(--teal)"></div>
    <div class="abs sub" style="left:280px;top:54px;font-weight:600">Presentation Sub - Title Goes Here</div>
    <div class="photo" role="img" aria-label="Collage of round photo cut-outs and rounded bars showing people at work" style="left:0;top:72px;width:540px;height:232px;background:linear-gradient(120deg,#f6f4f1 0%,#e7e3dc 35%,#dfe6ee 60%,#f4f6f8 100%)"></div>
  </div>
</section>

<main class="deck">

  <!-- 1 title -->
  <div class="slide slide-title">
    <div class="brand" style="left:22px;top:20px;font-size:14px"><i></i>qTorvix</div>
    <div class="abs" style="left:22px;top:40px;font-size:5.5px;color:var(--green);font-weight:600">Your Partner for Innovative Software Solutions</div>
    <div class="abs title" style="left:280px;top:22px">PRESENTATION TITLE</div>
    <div class="abs" style="left:280px;top:46px;width:260px;height:1px;background:var(--teal)"></div>
    <div class="abs sub" style="left:280px;top:54px;font-weight:600">Presentation Sub - Title Goes Here</div>
    <div class="photo" role="img" aria-label="Collage of round photo cut-outs and rounded bars showing people at work" style="left:0;top:72px;width:540px;height:232px;background:linear-gradient(120deg,#f6f4f1 0%,#e7e3dc 35%,#dfe6ee 60%,#f4f6f8 100%)"></div>
  </div>

  <!-- 2 photo and text -->
  <div class="slide">
    <div class="heading"><b>HEADING</b> GOES HERE</div>
    <div class="brand" style="right:16px;top:14px;font-size:10px"><i></i>qTorvix</div>
    <div class="top-rule"></div>
    <div class="abs" style="left:0;right:0;top:165px;height:139px;background:var(--teal)"></div>
    <div class="photo" role="img" aria-label="Photo of hands typing on a laptop beside a coffee cup" style="left:16px;top:72px;width:120px;height:105px;background:linear-gradient(135deg,#d9d2c6,#8d8b86 60%,#c9c3b8);box-shadow:6px 6px 0 #fff"></div>
    <div class="abs" style="left:190px;top:68px;font-size:8px;color:var(--ink)"><span style="color:var(--teal);font-weight:600">Text Here :</span>&nbsp; LOREM IPSUM DOLOR</div>
    <ul class="abs bullets body" style="left:250px;top:90px;font-size:6.5px;color:var(--ink)">
      <li>Lorem ipsum dolor sit amet.</li><li>Lorem ipsum dolor sit amet.</li><li>Lorem ipsum dolor sit amet.</li>
    </ul>
    <div class="abs body" style="left:190px;top:180px;width:335px;color:#fff;font-size:5.3px">
      <p>Lorem Ipsum is simply dummy text of the printing and typesetting industry. Lorem Ipsum has been the industry's standard dummy text ever since the 1500s, when an unknown printer took a galley of type and scrambled it to make a type specimen book. It has survived not only five centuries, but also the leap into electronic typesetting.</p>
      <p style="margin-top:5px">It was popularised in the 1960s with the release of transfer sheets containing Lorem Ipsum passages, and more recently with desktop publishing.</p>
      <p style="margin-top:5px">When an unknown printer took a galley of type and scrambled it to make a type specimen book. It has survived not only five centuries, but also the leap into electronic typesetting.</p>
    </div>
  </div>

  <!-- 3 banner and three icons -->
  <div class="slide">
    <div class="heading"><b>HEADING</b> GOES HERE</div>
    <div class="brand" style="right:16px;top:14px;font-size:10px"><i></i>qTorvix</div>
    <div class="abs" style="left:0;right:0;top:42px;height:95px;background:linear-gradient(90deg,var(--teal),#4f9aa9)"></div>
    <div class="abs" style="left:0;right:0;top:58px;text-align:center;color:#fff;font-family:'Montserrat',sans-serif;font-weight:600;font-size:11px;line-height:1.5">Lorem Ipsum is simply dummy text of the printing<br>Lorem Ipsum is simply dummy text</div>
    <svg class="abs" style="left:0;top:115px" width="540" height="120" viewBox="0 0 540 120">
      <g fill="var(--green)" stroke="#fff" stroke-width="3">
        <circle cx="90" cy="30" r="22"/><circle cx="270" cy="30" r="22"/><circle cx="450" cy="30" r="22"/>
      </g>
      <g fill="#fff">
        <circle cx="84" cy="24" r="4"/><circle cx="96" cy="24" r="4"/><rect x="78" y="30" width="24" height="9" rx="4"/>
        <circle cx="270" cy="22" r="5"/><rect x="262" y="29" width="16" height="11" rx="5"/>
        <circle cx="450" cy="30" r="10" fill="none" stroke="#fff" stroke-width="2"/><circle cx="450" cy="30" r="3"/>
      </g>
    </svg>
    <div class="abs body" style="left:40px;top:180px;width:100px;text-align:center;color:var(--ink)">Lorem Ipsum is simply dummy text of the printing and typesetting</div>
    <div class="abs body" style="left:220px;top:180px;width:100px;text-align:center;color:var(--ink)">Lorem Ipsum is simply dummy text of the printing and typesetting</div>
    <div class="abs body" style="left:400px;top:180px;width:100px;text-align:center;color:var(--ink)">Lorem Ipsum is simply dummy text of the printing and typesetting</div>
    <div class="footer">www.qtorvixlabs.com</div><div class="pageno">03</div>
  </div>

  <!-- 4 six items -->
  <div class="slide">
    <div class="heading"><b>HEADING</b> GOES HERE</div>
    <div class="brand" style="right:16px;top:14px;font-size:10px"><i></i>qTorvix</div>
    <div class="top-rule"></div>
    <svg class="abs" style="left:0;top:0" width="540" height="304" viewBox="0 0 540 304">
      <g fill="#fff" stroke="var(--teal)" stroke-width="1">
        <rect x="40" y="70" width="200" height="24" rx="2"/><rect x="40" y="143" width="200" height="24" rx="2"/><rect x="40" y="216" width="200" height="24" rx="2"/>
        <rect x="320" y="70" width="200" height="24" rx="2"/><rect x="320" y="143" width="200" height="24" rx="2"/><rect x="320" y="216" width="200" height="24" rx="2"/>
        <circle cx="38" cy="82" r="14"/><circle cx="38" cy="155" r="14"/><circle cx="38" cy="228" r="14"/>
        <circle cx="318" cy="82" r="14"/><circle cx="318" cy="155" r="14"/><circle cx="318" cy="228" r="14"/>
      </g>
      <g fill="var(--teal)">
        <circle cx="34" cy="79" r="2.5"/><circle cx="42" cy="79" r="2.5"/><rect x="30" y="83" width="16" height="5" rx="2.5"/>
        <circle cx="34" cy="152" r="2.5"/><circle cx="42" cy="152" r="2.5"/><rect x="30" y="156" width="16" height="5" rx="2.5"/>
        <circle cx="34" cy="225" r="2.5"/><circle cx="42" cy="225" r="2.5"/><rect x="30" y="229" width="16" height="5" rx="2.5"/>
        <circle cx="314" cy="79" r="2.5"/><circle cx="322" cy="79" r="2.5"/><rect x="310" y="83" width="16" height="5" rx="2.5"/>
        <circle cx="314" cy="152" r="2.5"/><circle cx="322" cy="152" r="2.5"/><rect x="310" y="156" width="16" height="5" rx="2.5"/>
        <circle cx="314" cy="225" r="2.5"/><circle cx="322" cy="225" r="2.5"/><rect x="310" y="229" width="16" height="5" rx="2.5"/>
      </g>
    </svg>
    <div class="abs sub" style="left:60px;top:61px">HEADING HERE</div><div class="abs body" style="left:60px;top:75px;width:170px;font-size:5px">Lorem Ipsum is simply dummy text of the printing and typesetting industry.</div>
    <div class="abs sub" style="left:60px;top:134px">HEADING HERE</div><div class="abs body" style="left:60px;top:148px;width:170px;font-size:5px">Lorem Ipsum is simply dummy text of the printing and typesetting industry.</div>
    <div class="abs sub" style="left:60px;top:207px">HEADING HERE</div><div class="abs body" style="left:60px;top:221px;width:170px;font-size:5px">Lorem Ipsum is simply dummy text of the printing and typesetting industry.</div>
    <div class="abs sub" style="left:340px;top:61px">HEADING HERE</div><div class="abs body" style="left:340px;top:75px;width:170px;font-size:5px">Lorem Ipsum is simply dummy text of the printing and typesetting industry.</div>
    <div class="abs sub" style="left:340px;top:134px">HEADING HERE</div><div class="abs body" style="left:340px;top:148px;width:170px;font-size:5px">Lorem Ipsum is simply dummy text of the printing and typesetting industry.</div>
    <div class="abs sub" style="left:340px;top:207px">HEADING HERE</div><div class="abs body" style="left:340px;top:221px;width:170px;font-size:5px">Lorem Ipsum is simply dummy text of the printing and typesetting industry.</div>
    <div class="footer">www.qtorvixlabs.com</div><div class="pageno">04</div>
  </div>

  <!-- 5 numbered -->
  <div class="slide">
    <div class="heading"><b>HEADING</b> GOES HERE</div>
    <div class="brand" style="right:16px;top:14px;font-size:10px"><i></i>qTorvix</div>
    <div class="top-rule"></div>
    <div class="abs" style="left:46px;top:62px"><div style="font-family:Montserrat,sans-serif;font-weight:700;font-size:10px;color:var(--ink)">01</div><div class="sub" style="margin-top:18px">HEADING HERE</div><div class="body" style="width:180px;margin-top:4px;font-size:5.5px">Lorem Ipsum is simply dummy text of the printing and typesetting industry. Lorem Ipsum has been the industry's standard dummy text ever since the 1500s.</div></div>
    <div class="abs" style="left:310px;top:62px"><div style="font-family:Montserrat,sans-serif;font-weight:700;font-size:10px;color:var(--ink)">02</div><div class="sub" style="margin-top:18px">HEADING HERE</div><div class="body" style="width:180px;margin-top:4px;font-size:5.5px">Lorem Ipsum is simply dummy text of the printing and typesetting industry. Lorem Ipsum has been the industry's standard dummy text ever since the 1500s.</div></div>
    <div class="abs" style="left:46px;top:172px"><div style="font-family:Montserrat,sans-serif;font-weight:700;font-size:10px;color:var(--ink)">03</div><div class="sub" style="margin-top:18px">HEADING HERE</div><div class="body" style="width:180px;margin-top:4px;font-size:5.5px">Lorem Ipsum is simply dummy text of the printing and typesetting industry. Lorem Ipsum has been the industry's standard dummy text ever since the 1500s.</div></div>
    <div class="abs" style="left:310px;top:172px"><div style="font-family:Montserrat,sans-serif;font-weight:700;font-size:10px;color:var(--ink)">04</div><div class="sub" style="margin-top:18px">HEADING HERE</div><div class="body" style="width:180px;margin-top:4px;font-size:5.5px">Lorem Ipsum is simply dummy text of the printing and typesetting industry. Lorem Ipsum has been the industry's standard dummy text ever since the 1500s.</div></div>
    <div class="footer">www.qtorvixlabs.com</div><div class="pageno">05</div>
  </div>

  <!-- 6 three photos -->
  <div class="slide">
    <div class="heading"><b>HEADING</b> GOES HERE</div>
    <div class="brand" style="right:16px;top:14px;font-size:10px"><i></i>qTorvix</div>
    <div class="top-rule"></div>
    <div class="photo" role="img" aria-label="Photo of a laptop on a desk showing charts" style="left:16px;top:88px;width:145px;height:86px;background:linear-gradient(135deg,#e6e6e4,#6f747a 55%,#c8c6c0)"></div>
    <div class="photo" role="img" aria-label="Photo of team hands stacked together over a table" style="left:198px;top:88px;width:145px;height:86px;background:linear-gradient(135deg,#4a3b2f,#a07b5c 50%,#3b3b3d)"></div>
    <div class="photo" role="img" aria-label="Photo of colleagues talking in an office" style="left:380px;top:88px;width:145px;height:86px;background:linear-gradient(135deg,#d8d2c8,#7d6a5c 50%,#b9b3aa)"></div>
    <div class="abs body" style="left:16px;top:182px;width:145px;text-align:center;color:var(--ink)">Lorem Ipsum is simply dummy text of the printing and typesetting industry.</div>
    <div class="abs body" style="left:198px;top:182px;width:145px;text-align:center;color:var(--ink)">Lorem Ipsum is simply dummy text of the printing and typesetting industry.</div>
    <div class="abs body" style="left:380px;top:182px;width:145px;text-align:center;color:var(--ink)">Lorem Ipsum is simply dummy text of the printing and typesetting industry.</div>
    <div class="btn" style="left:16px;top:210px;width:145px">HEADING HERE</div>
    <div class="btn" style="left:198px;top:210px;width:145px">HEADING HERE</div>
    <div class="btn" style="left:380px;top:210px;width:145px">HEADING HERE</div>
    <div class="footer">www.qtorvixlabs.com</div><div class="pageno">06</div>
  </div>

  <!-- 7 text with side photo -->
  <div class="slide">
    <div class="heading"><b>HEADING</b> GOES HERE</div>
    <div class="photo" role="img" aria-label="Photo of a laptop, camera lens and headphones on a white desk" style="left:255px;top:0;width:285px;height:304px;background:linear-gradient(160deg,#f3f3f3,#cfd1d3 45%,#5d6064 75%,#d9dadb)"></div>
    <div class="brand" style="right:16px;top:14px;font-size:10px"><i></i>qTorvix</div>
    <div class="abs body" style="left:16px;top:52px;width:225px;font-size:5.5px">
      <p>Lorem Ipsum is simply dummy text of the printing and typesetting industry. Lorem Ipsum has been the industry's standard dummy text ever since the 1500s, when an unknown printer took a galley of type and scrambled it to make a type specimen book. It has survived not only five centuries, but also the leap into electronic typesetting, remaining essentially unchanged.</p>
      <p style="margin-top:8px">It was popularised in the 1960s with the release of transfer sheets containing Lorem Ipsum passages, and more recently with desktop publishing software including many versions of Lorem Ipsum.</p>
      <p style="margin-top:8px">Lorem Ipsum is simply dummy text of the printing and typesetting industry. Lorem Ipsum has been the industry's standard dummy text ever since the 1500s, when an unknown printer took a galley of type and scrambled it to make a type specimen book.</p>
    </div>
    <div class="footer" style="right:300px">www.qtorvixlabs.com</div><div class="pageno">07</div>
  </div>

  <!-- 8 text and two boxes -->
  <div class="slide">
    <div class="heading"><b>HEADING</b> GOES HERE</div>
    <div class="brand" style="right:16px;top:14px;font-size:10px"><i></i>qTorvix</div>
    <div class="abs sub" style="left:16px;top:42px">HEADING HERE</div>
    <div class="abs body" style="left:16px;top:54px;width:508px;font-size:5.3px">
      <p>Lorem Ipsum is simply dummy text of the printing and typesetting industry. Lorem Ipsum has been the industry's standard dummy text ever since the 1500s, when an unknown printer took a galley of type and scrambled it to make a type specimen book.</p>
      <p style="margin-top:6px">Lorem Ipsum is simply dummy text of the printing and typesetting industry. Lorem Ipsum has been the industry's standard dummy text.</p>
      <p style="margin-top:6px">Lorem Ipsum is simply dummy text of the printing and typesetting industry. Lorem Ipsum has been the industry's standard dummy text ever since the 1500s, when an unknown printer took a galley of type and scrambled it to make a type specimen book.</p>
    </div>
    <div class="abs" style="left:46px;top:180px;width:190px;height:70px;background:var(--green-soft)"></div>
    <div class="abs" style="left:304px;top:180px;width:190px;height:70px;background:var(--green-soft)"></div>
    <div class="btn" style="left:54px;top:172px;width:174px;font-size:6px;line-height:14px">HEADING GOES HERE</div>
    <div class="btn" style="left:312px;top:172px;width:174px;font-size:6px;line-height:14px">HEADING GOES HERE</div>
    <div class="abs body" style="left:56px;top:194px;width:170px;text-align:center;font-size:5.3px">Lorem Ipsum is simply dummy text of the printing and typesetting industry. Lorem Ipsum has been the industry's standard dummy text ever since the 1500s, when an unknown printer took a galley of type.</div>
    <div class="abs body" style="left:314px;top:194px;width:170px;text-align:center;font-size:5.3px">Lorem Ipsum is simply dummy text of the printing and typesetting industry. Lorem Ipsum has been the industry's standard dummy text ever since the 1500s, when an unknown printer took a galley of type.</div>
    <div class="footer">www.qtorvixlabs.com</div><div class="pageno">08</div>
  </div>

  <!-- 9 banner photo with bullets -->
  <div class="slide">
    <div class="photo" role="img" aria-label="Photo of glasses resting on a closed laptop on a wooden desk" style="left:0;top:0;width:540px;height:108px;background:linear-gradient(90deg,#cfd6db 0%,#e8e6e2 40%,#b88a5a 70%,#8e623b 100%)"></div>
    <div class="abs" style="left:22px;top:108px;width:220px;height:5px;background:var(--green)"></div>
    <div class="abs body" style="left:22px;top:126px;width:220px;font-size:5.3px">
      <p>Lorem Ipsum is simply dummy text of the printing and typesetting industry. Lorem Ipsum has been the industry's standard dummy text ever since the 1500s, when an unknown printer took a galley of type and scrambled it to make a type specimen book.</p>
      <p style="margin-top:6px">Lorem Ipsum is simply dummy text of the printing and typesetting industry. Lorem Ipsum has been the industry's standard dummy text.</p>
      <p style="margin-top:6px">Lorem Ipsum is simply dummy text of the printing and typesetting industry. Lorem Ipsum has been the industry's standard dummy text ever since the 1500s, when an unknown printer took a galley of type and scrambled it to make a type specimen book.</p>
    </div>
    <div class="abs sub" style="left:308px;top:126px;text-decoration:underline;font-size:6px">HEADING GOES HERE</div>
    <ul class="abs bullets body" style="left:308px;top:144px;width:210px;font-size:5.3px">
      <li>Lorem Ipsum is simply dummy text of the printing and typesetting industry. Lorem Ipsum has been the industry's standard.</li>
      <li>When an unknown printer took a galley of type and scrambled it to make a type specimen book.</li>
      <li>Lorem Ipsum is simply dummy text of the printing and typesetting industry. Lorem Ipsum has been the industry's standard dummy text.</li>
    </ul>
    <div class="footer">www.qtorvixlabs.com</div><div class="pageno">09</div>
  </div>

  <!-- 10 contact -->
  <div class="slide">
    <div class="abs" style="left:0;top:0;width:285px;height:304px;background:var(--teal)"></div>
    <div class="abs" style="left:40px;top:34px;color:#fff;font-family:Montserrat,sans-serif;font-weight:700;font-size:12px">CONTACT INFO</div>
    <div class="abs" style="left:40px;top:54px;width:120px;height:1px;background:#fff"></div>
    <svg class="abs" style="left:0;top:0" width="540" height="304" viewBox="0 0 540 304">
      <g fill="var(--green)" stroke="#fff" stroke-width="2">
        <circle cx="285" cy="100" r="13"/><circle cx="285" cy="170" r="13"/><circle cx="285" cy="240" r="13"/>
      </g>
      <path d="M285 93a5 5 0 0 1 5 5c0 4-5 9-5 9s-5-5-5-9a5 5 0 0 1 5-5z" fill="#fff"/>
      <circle cx="285" cy="98" r="1.8" fill="var(--green)"/>
      <rect x="280.5" y="162" width="9" height="16" rx="1.5" fill="#fff"/>
      <rect x="282" y="164" width="6" height="10" fill="var(--green)"/>
      <rect x="278" y="235" width="14" height="10" rx="1" fill="#fff"/>
      <path d="M278 235l7 5.5 7-5.5" fill="none" stroke="var(--green)" stroke-width="1.2"/>
    </svg>
    <div class="abs" style="left:320px;top:96px;font-family:Montserrat,sans-serif;font-weight:600;font-size:7px;color:var(--ink)">ADDRESS GOES HERE</div>
    <div class="abs" style="left:320px;top:166px;font-family:Montserrat,sans-serif;font-weight:600;font-size:7px;color:var(--ink)">PHONE NO GOES HERE</div>
    <div class="abs" style="left:320px;top:236px;font-family:Montserrat,sans-serif;font-weight:600;font-size:7px;color:var(--ink)">EMAIL GOES HERE</div>
  </div>

</main>
</body>
</html>
```